Shopping center investment profile

We need to design a two-page 8.5" x 11" brochure that can be used as a template for profiling our shopping centers and demonstrating our track record to investors.

Our company (Pelvoran Real Estate Investments) owns retail shopping centers in the southwestern United States. Our website is www.kelvistrand.example, but we will be redesigning and modernizing the website and logo in the near future, so please do not use the color schemes or framework of the website for the brochure.

Our investors are institutional and high net worth investors who typically have an existing relationship with our company. They are determining whether to invest multi-millions of dollars in a shopping center opportunity, so the brochure needs to be professional, very high quality and provide key information about the specific property.
Updates

Additional guidance on color scheme:

We would like to see a Blue (something like Hex #5A61BC) and Gold (Hex #EDB215) or (Hex #DDA24B) color scheme with some Black accents 

Thank you!

Target Market(s)

Our target audiences are institutional investors, high net-worth individuals, financial firms and medium to large commercial real estate companies.

Industry/Entity Type

Investment

Requirements
Must have
• Clean and modern look with corresponding fonts and colors.
• Incorporates the information found in the attached "Morrowick Commons profile" Pages or PDF file.
• Final file design files that can be modified easily
Nice to have
• Two examples of industry brochures are attached. These are examples of the professional quality that we are looking for, not necessarily the design or format.

```html
<!DOCTYPE html>
<html lang="en">
<head>
<meta charset="utf-8">
<title>Morrowick Commons Property Profile</title>
<link href="https://fonts.googleapis.com/css2?family=Montserrat:wght@600;700;800&family=Oswald:wght@500;600&display=swap" rel="stylesheet">
<style>
  :root{
    --sky-top:#1f3fb8;
    --sky-mid:#4f86d6;
    --sky-low:#a9c4e6;
    --heading-navy:#1c2b62;
    --heading-slate:#2f4a7e;
    --row-purple:#5a37a6;
    --row-violet:#8a4cc0;
    --row-pale:rgba(214,220,244,.82);
    --ink-dark:#36385a;
    --total-cyan:#1ea3e4;
    --split-amber:#c98640;
    --structure-yellow:rgba(236,232,52,.85);
    --bullet-magenta:#b3176f;
    --band-magenta:#9b2b8d;
    --title-pale:#f1d9ec;
    --building-brown:#8a5a3c;
    --building-tan:#c79c7c;
    --page-bg:#6e6e6e;
  }
  *{box-sizing:border-box;margin:0;padding:0}
  html,body{width:1200px;height:829px;overflow:hidden;background:var(--page-bg)}
  body{font-family:"Montserrat",Arial,sans-serif}
  .brochure{position:relative;width:1200px;height:829px;overflow:hidden}
  .sky{position:absolute;inset:0;background:linear-gradient(170deg,var(--sky-top) 0%,var(--sky-mid) 40%,var(--sky-low) 70%,#d4dfee 100%)}
  .building{position:absolute;left:380px;top:430px;width:820px;height:300px;
    background:linear-gradient(90deg,var(--building-tan) 0%,var(--building-brown) 55%,#6e4630 100%);
    clip-path:polygon(0 62%,20% 45%,40% 20%,58% 0,100% 8%,100% 100%,0 100%)}
  .lot{position:absolute;left:0;top:690px;width:1200px;height:40px;background:#5b5e6a}
  .panel{position:absolute;left:70px;width:426px}
  .section-title{display:inline-block;background:var(--heading-navy);color:#fff;font-weight:800;font-size:20px;padding:3px 16px 3px 12px}
  .info-table{list-style:none;margin-top:2px}
  .info-row{display:flex;justify-content:space-between;align-items:center;height:31px;padding:0 12px;font-weight:700;font-size:15px;margin-bottom:1px}
  .info-row.purple{background:linear-gradient(90deg,var(--row-purple),var(--row-violet));color:#fff}
  .info-row.pale{background:var(--row-pale);color:var(--ink-dark)}
  .info-row.tall{height:48px;line-height:1.15}
  .info-row.total{background:var(--total-cyan);color:#fff}
  .info-row.split{background:var(--split-amber);color:#fff}
  .structure{display:flex;gap:24px;background:var(--structure-yellow);color:var(--ink-dark);font-weight:700;padding:8px 12px;height:72px}
  .structure-label{font-size:15px}
  .structure ul{list-style:none;font-size:13.5px;line-height:1.35}
  .structure li::before{content:"• "}
  .summary{top:80px}
  .investment{top:354px}
  .notes{position:absolute;left:598px;width:560px}
  .notes .section-title{background:var(--heading-slate);font-size:19px}
  .ticks{list-style:none;margin-top:10px;color:var(--bullet-magenta);font-weight:700;font-size:13.2px;line-height:1.2}
  .ticks li{position:relative;padding-left:17px}
  .ticks svg{position:absolute;left:0;top:3px}
  .opportunity{top:100px}
  .results{top:325px}
  .band{position:absolute;left:0;top:725px;width:1200px;height:104px;background:var(--band-magenta);text-align:center}
  .band h1{font-family:"Oswald",Arial,sans-serif;font-weight:600;font-size:42px;letter-spacing:1px;color:var(--title-pale);margin-top:6px;line-height:1.1}
  .band p{font-weight:800;font-size:19px;color:#fff;letter-spacing:.5px}
</style>
</head>
<body>
<main class="brochure">
  <div class="sky" role="img" aria-label="Bright blue sky with light clouds"></div>
  <div class="building" role="img" aria-label="Rendering of the retail shopping center with storefronts and signage tower"></div>
  <div class="lot" role="img" aria-label="Parking lot in front of the shopping center"></div>

  <section class="panel summary">
    <h2 class="section-title">Summarry</h2>
    <ul class="info-table">
      <li class="info-row purple"><span>Property Type</span><span>Shopping Center</span></li>
      <li class="info-row pale"><span>Size</span><span>79,490 sq ft</span></li>
      <li class="info-row purple"><span>Purchased</span><span>April 2011</span></li>
      <li class="info-row pale"><span>Total Investment</span><span>$X,XXX,XXX</span></li>
      <li class="info-row purple"><span>Purchase Occupancy</span><span>8.39%</span></li>
      <li class="info-row pale"><span>Current Occupancy</span><span>97.29%</span></li>
      <li class="info-row purple tall"><span>Projected 5-year IRR<br>(Unleveraged)</span><span>XX.XX%</span></li>
    </ul>
  </section>

  <section class="panel investment">
    <h2 class="section-title">Investment Information</h2>
    <ul class="info-table">
      <li class="info-row purple"><span>Purchase Price</span><span>$X,XXX,XXX</span></li>
      <li class="info-row pale"><span>Sponsor Acquisition Fee</span><span>$XX,XXX</span></li>
      <li class="info-row purple"><span>Painting and Landscape</span><span>$XXX,XXX</span></li>
      <li class="info-row pale"><span>TI/LC Reserve</span><span>$X,XXX,XXX</span></li>
      <li class="info-row purple"><span>Operating Expenses</span><span>$XXX,XXX</span></li>
      <li class="info-row total"><span>Total Cash Investment</span><span></span></li>
      <li class="info-row split"><span>Investor/Sponsor Split</span><span>XX% / XX%</span></li>
    </ul>
    <div class="structure">
      <span class="structure-label">Structure</span>
      <ul>
        <li>Cash Flow Pari Passu</li>
        <li>Acquisition Fee</li>
        <li>Management Fee</li>
      </ul>
    </div>
  </section>

  <section class="notes opportunity">
    <h2 class="section-title">Opportunity</h2>
    <ul class="ticks">
      <li><svg width="11" height="10" viewBox="0 0 11 10"><path d="M1 5l3 3 6-7" fill="none" stroke="currentColor" stroke-width="2"/></svg>Bank owned property with attractive purchase price</li>
      <li><svg width="11" height="10" viewBox="0 0 11 10"><path d="M1 5l3 3 6-7" fill="none" stroke="currentColor" stroke-width="2"/></svg>Strong relationship with seller's broker and decision makers</li>
      <li><svg width="11" height="10" viewBox="0 0 11 10"><path d="M1 5l3 3 6-7" fill="none" stroke="currentColor" stroke-width="2"/></svg>Redevelopment upside with management and leasing</li>
      <li><svg width="11" height="10" viewBox="0 0 11 10"><path d="M1 5l3 3 6-7" fill="none" stroke="currentColor" stroke-width="2"/></svg>No major renovations required</li>
      <li><svg width="11" height="10" viewBox="0 0 11 10"><path d="M1 5l3 3 6-7" fill="none" stroke="currentColor" stroke-width="2"/></svg>Dunmere location has very strong population, education and income demographics</li>
      <li><svg width="11" height="10" viewBox="0 0 11 10"><path d="M1 5l3 3 6-7" fill="none" stroke="currentColor" stroke-width="2"/></svg>Adjacent to premier 2,500-residence master planned community of Harlow Springs</li>
      <li><svg width="11" height="10" viewBox="0 0 11 10"><path d="M1 5l3 3 6-7" fill="none" stroke="currentColor" stroke-width="2"/></svg>Strong employment area with the new Northvale Gateway hospital and the adjacent Castlebrook Cancer center</li>
    </ul>
  </section>

  <section class="notes results">
    <h2 class="section-title">Results</h2>
    <ul class="ticks">
      <li><svg width="11" height="10" viewBox="0 0 11 10"><path d="M1 5l3 3 6-7" fill="none" stroke="currentColor" stroke-width="2"/></svg>Stabilized the shopping center within three years, producing excellent results for investors</li>
      <li><svg width="11" height="10" viewBox="0 0 11 10"><path d="M1 5l3 3 6-7" fill="none" stroke="currentColor" stroke-width="2"/></svg>Transformed the center into a vibrant destination that the surrounding community is excited about</li>
      <li><svg width="11" height="10" viewBox="0 0 11 10"><path d="M1 5l3 3 6-7" fill="none" stroke="currentColor" stroke-width="2"/></svg>Transitioned legacy tenants to upgrade the business operators</li>
      <li><svg width="11" height="10" viewBox="0 0 11 10"><path d="M1 5l3 3 6-7" fill="none" stroke="currentColor" stroke-width="2"/></svg>Reduced the shopping center's operating expenses by XX%</li>
    </ul>
  </section>

  <footer class="band">
    <h1>MORROWICK COMMONS PROPERTY PROFILE</h1>
    <p>SWC OF TESSALY RD AND CORRIN RD - DUNMERE, ARIZONA</p>
  </footer>
</main>
</body>
</html>
```